Copperleaf Motorized Shade Business Card

Hello, we've had our logo made. Now we are looking for a clean and cool looking business card. One side can just be the logo with any design elements that might look good with it. The other side will be Name, Phone Number and Email. There will not be an address on the card.

```html
<!DOCTYPE html>
<html lang="en">
<head>
<meta charset="UTF-8">
<title>Copperleaf Motorized Shade Business Card</title>
<link rel="stylesheet" href="https://fonts.googleapis.com/css2?family=Montserrat:wght@500;600;700;800&display=swap">
<style>
  :root {
    --backdrop: #9b9b9b;
    --navy: #173f73;
    --gold: #f6b31b;
    --white: #ffffff;
    --contact-blue: #2c8fd0;
  }
  * { box-sizing: border-box; margin: 0; padding: 0; }
  html, body { width: 1200px; height: 800px; overflow: hidden; }
  body {
    background: var(--backdrop);
    font-family: "Montserrat", sans-serif;
    position: relative;
  }
  .card {
    position: absolute;
    top: 260px;
    width: 490px;
    height: 278px;
  }
  .card--front { left: 90px; background: var(--white); }
  .card--back { left: 620px; background: var(--navy); }

  .front-brand {
    position: absolute;
    left: 20px;
    top: 36px;
    display: flex;
    align-items: center;
    gap: 8px;
    color: var(--navy);
    font-weight: 800;
  }
  .brand-square { width: 14px; height: 14px; background: currentColor; flex: none; }
  .brand-text { display: flex; flex-direction: column; line-height: 1; }
  .front-brand .brand-name { font-size: 24px; letter-spacing: 0.5px; }
  .front-brand .brand-tag { font-size: 8px; letter-spacing: 2.4px; margin-top: 4px; }

  .name-band {
    position: absolute;
    left: 0; top: 140px;
    width: 100%; height: 50px;
    background: var(--navy);
    text-align: center;
    padding-top: 9px;
  }
  .person-name { color: var(--gold); font-weight: 700; font-size: 18px; line-height: 1.1; }
  .person-title { color: var(--white); font-weight: 600; font-size: 7px; letter-spacing: 1px; margin-top: 2px; }

  .contacts {
    position: absolute;
    left: 106px; top: 218px;
    display: grid;
    grid-template-columns: auto auto;
    column-gap: 40px;
    row-gap: 8px;
    color: var(--contact-blue);
    font-size: 10.5px;
    font-weight: 600;
    letter-spacing: 0.5px;
  }
  .contact-item { display: flex; align-items: center; gap: 8px; white-space: nowrap; }
  .contact-item svg { width: 12px; height: 12px; flex: none; }

  .back-brand {
    position: absolute;
    left: 0; right: 0; top: 100px;
    text-align: center;
    color: var(--gold);
    font-weight: 800;
    line-height: 1;
  }
  .back-brand .brand-name { font-size: 38px; letter-spacing: 1px; }
  .back-brand .brand-tag { font-size: 10px; letter-spacing: 3.6px; margin-top: 10px; }
  .back-web {
    position: absolute;
    left: 0; right: 0; top: 254px;
    text-align: center;
    color: var(--gold);
    font-size: 10.5px;
    font-weight: 700;
    letter-spacing: 2.6px;
  }
</style>
</head>
<body>
  <section class="card card--front">
    <div class="front-brand">
      <span class="brand-square"></span>
      <div class="brand-text">
        <span class="brand-name">COPPERLEAF</span>
        <span class="brand-tag">MOTORIZED SHADE</span>
      </div>
    </div>

    <div class="name-band">
      <p class="person-name">Dana Whitfield</p>
      <p class="person-title">PRESIDENT</p>
    </div>

    <div class="contacts">
      <div class="contact-item">
        <svg viewBox="0 0 12 12" fill="#f6b31b"><path d="M2.5 1h2l1 2.5-1.3 1a6.5 6.5 0 0 0 3.3 3.3l1-1.3 2.5 1v2a1 1 0 0 1-1 1A9.5 9.5 0 0 1 1.5 2a1 1 0 0 1 1-1z"/></svg>
        <span>555. 208. 4417</span>
      </div>
      <div class="contact-item">
        <svg viewBox="0 0 12 12" fill="#f6b31b"><rect x="1" y="2.5" width="10" height="7" rx="1"/><path d="M1.5 3l4.5 3.5L10.5 3" stroke="#fff" stroke-width="1" fill="none"/></svg>
        <span>hello@copperleafshadeco.com</span>
      </div>
      <div class="contact-item">
        <svg viewBox="0 0 12 12" fill="none" stroke="#f6b31b" stroke-width="1.4"><rect x="3.5" y="1" width="5" height="10" rx="1"/></svg>
        <span>555. 806. 7144</span>
      </div>
      <div class="contact-item">
        <svg viewBox="0 0 12 12" fill="none" stroke="#f6b31b" stroke-width="1.1"><circle cx="6" cy="6" r="5"/><ellipse cx="6" cy="6" rx="2.2" ry="5"/><path d="M1 6h10"/></svg>
        <span>www.copperleafshadeco.com</span>
      </div>
    </div>
  </section>

  <section class="card card--back">
    <div class="back-brand">
      <div class="brand-name">COPPERLEAF</div>
      <div class="brand-tag">MOTORIZED SHADE</div>
    </div>
    <p class="back-web">WWW.COPPERLEAFSHADECO.COM</p>
  </section>
</body>
</html>
```